Elegant Business Cards & Letterhead

We will need the following that need to be designed: Letterhead and Business Cards, there winer will be re-hired for the balance of our stationary needs. Text for the cards and letterheads:

- Corporate Card instead of name
- landline: +971 (4) 362 7041
- mobile: +971 56 2819 605
- 800TUTOR
- email: dubai@velmora-lune.com
- www.velmora-lune.com
- PO Box 387261
Address: Castellan Heights Suite 1708, Dubai UAE

Thank you

Target Market(s)

VIPs, HNWI, High-end Families.

Industry/Entity Type

Luxury Market

Font styles to use
Other font styles liked:
• as explained

Colors

Designer to choose only greyscale colors for use in the design.

Requirements
Must have
• Elegant, Simple, Luxurious, Minimalistic
Nice to have
• Luxury, Golds, Engravings,
Should not have
• Much colors, funky,

```html
<!DOCTYPE html>
<html lang="en">
<head>
<meta charset="utf-8">
<title>Velmora Lune – Business Card</title>
<link rel="stylesheet" href="https://fonts.googleapis.com/css2?family=Cinzel:wght@500&family=Josefin+Sans:wght@300&display=swap">
<style>
  :root {
    --backdrop: #6e6e70;
    --card: #221f20;
    --gold: #d9bb7a;
    --gold-light: #f9efaa;
    --gold-mid: #e6c98a;
    --gold-dark: #a88e5a;
    --ink-light: #f2f2f2;
  }
  * { margin: 0; padding: 0; box-sizing: border-box; }
  html, body {
    width: 1200px;
    height: 1200px;
    overflow: hidden;
    background: var(--backdrop);
  }
  .canvas {
    position: relative;
    width: 1200px;
    height: 1200px;
  }
  .card {
    position: absolute;
    left: 302px;
    width: 595px;
    height: 364px;
    background: var(--card);
    border-radius: 19px;
    overflow: hidden;
  }
  .card--front { top: 215px; }
  .card--back { top: 674px; }
  .card__band {
    position: absolute;
    left: 0;
    bottom: 0;
    width: 100%;
    height: 26px;
    background: linear-gradient(90deg, #e3cc8c 0%, var(--gold-light) 22%, var(--gold-mid) 70%, #dcb97a 85%, var(--gold-dark) 100%);
  }
  .brand-name {
    position: absolute;
    font-family: "Cinzel", "Times New Roman", serif;
    font-weight: 500;
    color: var(--gold);
    white-space: nowrap;
    line-height: 1;
  }
  .card--front .brand-name {
    left: 71px;
    top: 48px;
    font-size: 34px;
  }
  .card--back .brand-name {
    left: 0;
    width: 100%;
    text-align: center;
    top: 158px;
    font-size: 43px;
  }
  .contact-list {
    position: absolute;
    left: 71px;
    top: 173px;
    list-style: none;
    font-family: "Josefin Sans", "Helvetica Neue", sans-serif;
    font-weight: 300;
    font-size: 15.5px;
    color: var(--ink-light);
    line-height: 21px;
    letter-spacing: 0.3px;
  }
  .contact-list li { display: flex; }
  .contact-list .label { width: 36px; flex: none; }
  .contact-list .label--wide { width: auto; margin-right: 4px; }
  .website {
    position: absolute;
    left: 0;
    width: 100%;
    bottom: 35px;
    text-align: center;
    font-family: "Josefin Sans", "Helvetica Neue", sans-serif;
    font-weight: 300;
    font-size: 16px;
    letter-spacing: 0.6px;
    color: var(--ink-light);
  }
</style>
</head>
<body>
<main class="canvas">
  <section class="card card--front" aria-label="Business card front">
    <div class="brand-name">VELMORA LUNE</div>
    <ul class="contact-list">
      <li><span class="label">T -</span><span>+971 (4) 362 7041</span></li>
      <li><span class="label">F -</span><span>+971 (56) 2819 605</span></li>
      <li><span class="label">E -</span><span>dubai@velmora-lune.com</span></li>
      <li><span class="label">W -</span><span>www.velmora-lune.com</span></li>
      <li><span class="label label--wide">PO -</span><span>387261</span></li>
      <li><span class="label">L -</span><span>Castellan Heights Suite 1708,<br>Dubai UAE</span></li>
    </ul>
    <div class="card__band"></div>
  </section>

  <section class="card card--back" aria-label="Business card back">
    <div class="brand-name">VELMORA LUNE</div>
    <p class="website">www.velmora-lune.com</p>
    <div class="card__band"></div>
  </section>
</main>
</body>
</html>
```